Marlow Crest Group (Real Estate and Investment)

A high end, clean design.
We are a real estate company with sales, asset management and investment divisions. We want to use a black and white scheme which is really high end feel. The back of the card can just be the logo (black background with the white writing) as we will probably emboss this when we print)

Target Market(s)

High level investors, high end houses for sale

Industry/Entity Type

Business

Contact Information for Business Card

Name, position, phone number and email address
Glen Varley, Managing Director, 0437259064 and glen@marlowcrest-example.com.au

Requirements
Must have
• Back of the card to be the black background with the white writing (as per the attached images). Would like the capacity to emboss the writing and logo

```html
<!DOCTYPE html>
<html lang="en">
<head>
<meta charset="utf-8">
<title>Marlow Crest Group – Business Card</title>
<link rel="stylesheet" href="https://fonts.googleapis.com/css2?family=Jost:wght@400;500;600&family=Poppins:wght@300&display=swap">
<style>
  :root {
    --stage: #2c3031;
    --card-black: #0b0b0b;
    --card-white: #ffffff;
    --ink: #111111;
    --ink-soft: #2a2a2a;
    --divider: #e2e2e2;
    --facet-light: #ffffff;
    --facet-mid: #ededed;
  }
  * { margin: 0; padding: 0; box-sizing: border-box; }
  html, body {
    width: 1200px; height: 1200px; overflow: hidden;
    background: var(--stage);
  }
  .canvas { position: relative; width: 1200px; height: 1200px; }

  .card { position: absolute; left: 215px; width: 770px; height: 462px; }

  /* back of card */
  .card-back { top: 110px; background: var(--card-black); }
  .brand-mark {
    position: absolute; left: 527px - 215px;
  }
  .brand-circle {
    position: absolute; left: 313px; top: 128px;
    width: 144px; height: 144px;
    border: 2px solid var(--card-white); border-radius: 50%;
  }
  .brand-name {
    position: absolute; left: 0; right: 0; top: 296px;
    text-align: center;
    font-family: "Poppins", sans-serif; font-weight: 300;
    font-size: 36px; letter-spacing: 0.5px;
    color: var(--card-white);
  }

  /* front of card */
  .card-front { top: 649px; background: var(--card-white); overflow: hidden; }
  .facet-texture {
    position: absolute; inset: 0;
    background: linear-gradient(180deg, var(--facet-light) 0%, var(--facet-mid) 45%, var(--facet-light) 100%);
    opacity: 0.7;
  }
  .column-divider {
    position: absolute; left: 348px; top: 50px; width: 4px; height: 328px;
    background: linear-gradient(90deg, var(--divider), rgba(226,226,226,0));
  }
  .identity {
    position: absolute; left: 40px; width: 294px; top: 200px;
    text-align: right;
  }
  .person-name {
    font-family: "Jost", sans-serif; font-weight: 400;
    font-size: 44px; line-height: 1; color: var(--ink);
    letter-spacing: 0.5px;
  }
  .person-name strong { font-weight: 600; }
  .person-role {
    font-family: "Jost", sans-serif; font-weight: 400;
    font-size: 19px; line-height: 1; color: var(--ink-soft);
    letter-spacing: 0.6px; margin-top: 6px; padding-right: 26px;
    text-align: center; padding-left: 30px;
  }
  .contact-list { position: absolute; left: 384px; top: 124px; list-style: none; }
  .contact-item {
    display: flex; align-items: center; height: 32px;
    font-family: "Jost", sans-serif; font-size: 19px; color: var(--ink);
  }
  .contact-item + .contact-item { margin-top: 63px; }
  .contact-icon { width: 32px; height: 28px; margin-right: 16px; flex: none; }
</style>
</head>
<body>
<main class="canvas">

  <section class="card card-back" aria-label="Card back">
    <div class="brand-circle"></div>
    <p class="brand-name">MARLOW CREST GROUP</p>
  </section>

  <section class="card card-front" aria-label="Card front">
    <div class="facet-texture" role="img" aria-label="Subtle white faceted diamond texture"></div>
    <div class="column-divider"></div>

    <div class="identity">
      <h1 class="person-name">GLEN <strong>VARLEY</strong></h1>
      <p class="person-role">MANAGING DIRECTOR</p>
    </div>

    <ul class="contact-list">
      <li class="contact-item">
        <svg class="contact-icon" viewBox="0 0 32 28" aria-hidden="true">
          <rect x="1" y="6" width="29" height="17" fill="#1a1a1a"/>
          <path d="M2 7 L15.5 17 L29 7" fill="none" stroke="#fff" stroke-width="2"/>
        </svg>
        glen@marlowcrest-example.com.au
      </li>
      <li class="contact-item">
        <svg class="contact-icon" viewBox="0 0 32 28" aria-hidden="true">
          <path d="M6 3 C4 4 2 6 3 10 C5 17 11 23 18 25 C22 26 24 24 25 22 L21 17 L17 19 C14 17 11 14 9 11 L11 7 Z" fill="#1a1a1a"/>
        </svg>
        0437259064
      </li>
      <li class="contact-item">
        <svg class="contact-icon" viewBox="0 0 32 28" aria-hidden="true">
          <circle cx="14" cy="14" r="12" fill="#1a1a1a"/>
          <ellipse cx="14" cy="14" rx="5" ry="11" fill="none" stroke="#fff" stroke-width="1.5"/>
          <line x1="3" y1="14" x2="25" y2="14" stroke="#fff" stroke-width="1.5"/>
        </svg>
        www.marlowcrest-example.com.au
      </li>
    </ul>
  </section>

</main>
</body>
</html>
```